Private Villa in Bali looking for a flyer design

We need a flyer design for a 2bedrooms private villa with pool in Bali, called VILLA SEKAR

Our villa is a private 2 bedrooms villa with private swimming pool, tranquil , luxurious, blending balinese and modern interiors , personal service and family home away from home
Out Motto : your blissful getaway

We would like an elegant, luxury and clean design

Colour scheme : BROWN, YELLOW/GOLD, GREY

It should have :
1/photo of the villa
2/ basic info of the villa
3/ location/address and location map of the villa

Villa Sekar
Banjar Tegalsari,
Kelodayu, Sumbawi
Bali - Indonesia

4/ website :
www.villasekarbintang

5/ email :
wulan@villasekarbintang.com

6/ Phone :
+852-57204916

I have attached some photos and the logo, please let me know if you need ai/eps file

Thank you . Please let me know if you need more information
Updates

-Trifold flyer on A4 size paper ( standard size flyer)

-Front page : Main photo and Logo
-Last page : Location map, email,website etc
-Page 2-4 : any design with photo and info from website 

Target Market(s)

Family, couples, honeymooners

Industry/Entity Type

It Service

Colors
ffc214
474747
9d9d9d

Requirements
Must have
• address, location map, website and email add, photos ( don't need to use all)

Trifold on A4 size paper double sided
Nice to have
• Trifold on A4 size paper
Should not have
• too many photos overlapping .

```html
<!DOCTYPE html>
<html lang="en">
<head>
<meta charset="utf-8">
<title>Villa Sekar – Flyer</title>
<link href="https://fonts.googleapis.com/css2?family=Oleo+Script:wght@700&family=Open+Sans:ital,wght@0,400;0,600;1,400&display=swap" rel="stylesheet">
<style>
  :root {
    --gold: #ffc214;
    --gold-deep: #e0a520;
    --charcoal: #474747;
    --ink: #1c1c1c;
    --grey: #9d9d9d;
    --paper: #f1f1f1;
    --backdrop: #f4e8d6;
    --white: #ffffff;
    --sky: #7d8fcf;
    --glow: #f3c77a;
    --roof: #3b3f66;
    --garden: #5a6a2e;
    --pool: #1e8fe0;
    --pool-deep: #1766b0;
    --stone: #b9ad98;
  }
  * { box-sizing: border-box; margin: 0; padding: 0; }
  html, body { width: 1200px; height: 800px; overflow: hidden; }
  body { background: var(--backdrop); font-family: "Open Sans", Arial, sans-serif; }

  .flyer {
    position: absolute; left: 365px; top: 62px;
    width: 470px; height: 676px;
    background: var(--paper);
    overflow: hidden;
    box-shadow: 0 10px 30px rgba(80, 60, 30, .18);
  }

  .hero {
    position: absolute; left: 0; top: 0; width: 470px; height: 380px;
    background:
      radial-gradient(ellipse 130px 110px at 90px 170px, rgba(255, 214, 140, .85), rgba(255, 214, 140, 0) 100%),
      radial-gradient(ellipse 90px 60px at 250px 190px, rgba(255, 200, 120, .7), rgba(255, 200, 120, 0) 100%),
      radial-gradient(ellipse 120px 90px at 430px 220px, rgba(90, 106, 46, .85), rgba(90, 106, 46, 0) 100%),
      linear-gradient(180deg,
        var(--sky) 0%, #a9b3dc 14%, var(--roof) 22%, #6a5a4a 30%,
        #b8894e 42%, #8a6a3e 56%, var(--stone) 62%, #c9c0ad 64%,
        var(--pool) 68%, #3aa8f0 78%, var(--pool-deep) 100%);
  }

  .brand-tile {
    position: absolute; left: 48px; top: 22px; width: 100px; height: 90px;
    background: var(--white);
    display: flex; flex-direction: column; align-items: center; justify-content: center; gap: 10px;
  }
  .brand-tile .mark { width: 26px; height: 26px; background: var(--gold-deep); }
  .brand-tile .brand-name { font-size: 14px; color: var(--charcoal); font-weight: 400; }

  .headline {
    position: absolute; right: 24px; top: 34px;
    font-family: "Oleo Script", cursive; font-weight: 700; font-size: 36px; color: var(--ink);
  }
  .headline .accent { color: var(--gold); }

  .gold-band {
    position: absolute; left: 0; top: 362px; width: 470px; height: 52px;
    background: var(--gold-deep);
  }

  .rooms { position: absolute; left: 46px; top: 300px; width: 400px; height: 222px; display: flex; }
  .room { width: 133.3px; height: 100%; padding: 12px 10px 0; }
  .room--dark { background: var(--ink); }
  .room--gold { background: var(--gold-deep); margin-top: 8px; }
  .room-title {
    font-family: "Oleo Script", cursive; font-weight: 700; font-size: 17px;
    color: var(--white); text-align: center; height: 44px; line-height: 30px;
  }
  .room-photo { width: 100%; height: 150px; }
  .room-photo--bed {
    background:
      radial-gradient(ellipse 60px 40px at 70% 30%, rgba(255, 240, 210, .9), rgba(255, 240, 210, 0)),
      linear-gradient(180deg, #8a6a4e 0%, #d9c6a6 40%, #f2ece2 70%, #5a3e2a 100%);
  }
  .room-photo--lounge {
    background:
      radial-gradient(ellipse 50px 40px at 80% 40%, rgba(255, 220, 120, .9), rgba(255, 220, 120, 0)),
      linear-gradient(180deg, #5a3420 0%, #a8642e 30%, #d8443a 55%, #e8d2b0 75%, #6a3a22 100%);
  }
  .room-photo--dining {
    background:
      radial-gradient(ellipse 60px 40px at 40% 25%, rgba(255, 236, 190, .9), rgba(255, 236, 190, 0)),
      linear-gradient(180deg, #e6d2ae 0%, #b8864a 40%, #7a5030 65%, #2a221c 100%);
  }

  .details { position: absolute; left: 38px; top: 548px; width: 410px; height: 110px; }
  .about { position: absolute; left: 0; top: 0; width: 140px; }
  .about h2 {
    font-family: "Oleo Script", cursive; font-weight: 700; font-size: 10px;
    color: var(--gold-deep); margin-bottom: 10px;
  }
  .about p { font-size: 7.4px; line-height: 10px; color: var(--grey); }

  .contact { position: absolute; left: 147px; top: 12px; width: 140px; list-style: none; }
  .contact li { display: flex; gap: 8px; font-size: 7.4px; color: var(--charcoal); line-height: 10px; margin-bottom: 5px; }
  .contact svg { flex: none; width: 9px; height: 9px; fill: var(--gold-deep); }

  .map-frame {
    position: absolute; left: 288px; top: 18px; width: 90px; height: 82px;
    background: var(--white); padding: 4px; box-shadow: 0 1px 3px rgba(0,0,0,.15);
  }
  .map-frame .map { width: 100%; height: 100%; background: linear-gradient(135deg, #e7e7e2 62%, #a8c4de 100%); }

  .footer-rule { position: absolute; left: 0; bottom: 12px; width: 470px; height: 5px; background: var(--gold); }
</style>
</head>
<body>
  <article class="flyer">
    <div class="hero" role="img" aria-label="Photo of the villa courtyard at dusk with the private pool and garden"></div>

    <div class="brand-tile">
      <span class="mark"></span>
      <span class="brand-name">Villa Sekar</span>
    </div>

    <h1 class="headline">Villa <span class="accent">Sekar</span></h1>

    <div class="gold-band"></div>

    <section class="rooms">
      <div class="room room--dark">
        <p class="room-title">Villa Sekar</p>
        <div class="room-photo room-photo--bed" role="img" aria-label="Photo of the master bedroom"></div>
      </div>
      <div class="room room--gold">
        <p class="room-title">Villa Sekar</p>
        <div class="room-photo room-photo--lounge" role="img" aria-label="Photo of the living room"></div>
      </div>
      <div class="room room--dark">
        <p class="room-title">Villa Sekar</p>
        <div class="room-photo room-photo--dining" role="img" aria-label="Photo of the dining area and kitchen"></div>
      </div>
    </section>

    <section class="details">
      <div class="about">
        <h2>Basic info of the villa</h2>
        <p>Our villa is a private 2 bedrooms villa with private swimming pool, tranquil , luxurious, blending balinese and modern interiors , personal service and family home away from home</p>
      </div>

      <ul class="contact">
        <li><svg viewBox="0 0 10 10"><rect x="2.5" y="0.5" width="5" height="9" rx="1"/></svg>+852-57204916</li>
        <li><svg viewBox="0 0 10 10"><circle cx="5" cy="5" r="4.5"/></svg>www.villasekarbintang</li>
        <li><svg viewBox="0 0 10 10"><rect x="0.5" y="2" width="9" height="6" rx="1"/></svg>wulan@villasekarbintang.com</li>
        <li><svg viewBox="0 0 10 10"><path d="M5 0.5 9.5 4.5H8V9.5H2V4.5H0.5Z"/></svg>
          <span>Villa Sekar<br>Banjar Tegalsari,<br>Kelodayu, Sumbawi<br>Bali - Indonesia</span></li>
      </ul>

      <div class="map-frame">
        <div class="map" role="img" aria-label="Location map of the villa"></div>
      </div>
    </section>

    <div class="footer-rule"></div>
  </article>
</body>
</html>
```